Bill board design For Marlowe’s Construction

Billboard Design Request
Please design the billboard to match the branding, colors, and overall feel of our website: Marlowe's Construction Website
MARLOWE’S CONSTRUCTION
CONCRETE BUILT FOR GENERATIONS
⭐ 5-Star Rated on Zorvix
Please Include:
* All three attached project photos
* Company logo(s)
* Phone Number: 555-214-7630
* Website: MarlowesConstruction.example
* Zorvix logo with 5-star rating graphic
* Chatterly logo
* Pixtoria logo
Service Area:
Kalamazoo • Battle Creek • Coldwater • Grand Rapids
Please arrange the photos and layout in whatever way creates the strongest visual impact and readability from the road. The company name, headline, phone number, and website should be highly visible at highway speeds.
The overall appearance should be clean, professional, premium, and consistent with our website branding while highlighting our reputation, craftsmanship, and quality concrete work.
People Driving By
Concrete Construction

```html
<!DOCTYPE html>
<html lang="en">
<head>
<meta charset="utf-8">
<title>Marlowe’s Construction Billboard</title>
<link rel="stylesheet" href="https://fonts.googleapis.com/css2?family=Montserrat:wght@500;600;700;800&display=swap">
<style>
  :root {
    --page: #ffffff;
    --board-black: #1c1c1c;
    --deep-black: #0d0d0d;
    --header-grey: #3a3a3a;
    --brand-blue: #1596e8;
    --white: #ffffff;
    --photo-crew: #5e4a36;
    --photo-crew-light: #a58a66;
    --photo-garage: #b9aea3;
    --photo-garage-dark: #6e5f58;
    --photo-walk: #9a4e2c;
    --photo-walk-light: #c77a4d;
  }
  html, body {
    margin: 0;
    padding: 0;
    width: 1192px;
    height: 1200px;
    overflow: hidden;
    background: var(--page);
  }
  .billboard {
    position: absolute;
    left: 36px;
    top: 413px;
    width: 1120px;
    height: 373px;
    display: block;
  }
  .board-base { fill: var(--board-black); }
  .headline {
    font-family: "Montserrat", sans-serif;
    font-weight: 700;
    font-size: 42px;
    fill: var(--white);
  }
  .company-name {
    font-family: "Montserrat", sans-serif;
    font-weight: 600;
    fill: var(--brand-blue);
  }
  .company-name--main { font-size: 44px; letter-spacing: 1px; }
  .company-name--sub { font-size: 18px; letter-spacing: 6.2px; }
  .brand-square { fill: var(--brand-blue); }
  .phone-band { fill: var(--brand-blue); }
  .tagline {
    font-family: "Montserrat", sans-serif;
    font-weight: 800;
    font-size: 12px;
    letter-spacing: 2.2px;
    fill: var(--white);
  }
  .phone-number {
    font-family: "Montserrat", sans-serif;
    font-weight: 800;
    font-size: 40px;
    fill: var(--white);
  }
  .phone-icon-frame { fill: none; stroke: var(--white); stroke-width: 1.6; }
  .phone-icon { fill: none; stroke: var(--white); stroke-width: 1.6; stroke-linejoin: round; }
  .review-name {
    font-family: "Montserrat", sans-serif;
    font-weight: 600;
    font-size: 28px;
    fill: var(--white);
  }
  .review-rating {
    font-family: "Montserrat", sans-serif;
    font-weight: 500;
    font-size: 11px;
    fill: var(--white);
  }
  .website {
    font-family: "Montserrat", sans-serif;
    font-weight: 600;
    font-size: 17px;
    fill: var(--brand-blue);
  }
  .social-name {
    font-family: "Montserrat", sans-serif;
    font-weight: 600;
    font-size: 10px;
    fill: var(--white);
  }
</style>
</head>
<body>
<svg class="billboard" viewBox="0 0 1120 373" xmlns="http://www.w3.org/2000/svg">
  <defs>
    <linearGradient id="headerGrad" x1="0" y1="0" x2="1" y2="0">
      <stop offset="0" stop-color="var(--header-grey)"/>
      <stop offset="0.6" stop-color="var(--deep-black)"/>
      <stop offset="1" stop-color="var(--deep-black)"/>
    </linearGradient>
    <linearGradient id="reviewGrad" x1="0" y1="0" x2="1" y2="1">
      <stop offset="0" stop-color="#2a2a2a"/>
      <stop offset="1" stop-color="#151515"/>
    </linearGradient>
    <linearGradient id="footerGrad" x1="0" y1="0" x2="1" y2="0">
      <stop offset="0" stop-color="#2c2c2c"/>
      <stop offset="0.4" stop-color="var(--deep-black)"/>
      <stop offset="1" stop-color="var(--deep-black)"/>
    </linearGradient>
    <linearGradient id="crewGrad" x1="0" y1="0" x2="1" y2="1">
      <stop offset="0" stop-color="var(--photo-crew-light)"/>
      <stop offset="0.5" stop-color="#2a2522"/>
      <stop offset="1" stop-color="var(--photo-crew)"/>
    </linearGradient>
    <linearGradient id="garageGrad" x1="0" y1="0" x2="0" y2="1">
      <stop offset="0" stop-color="#8a9a6a"/>
      <stop offset="0.45" stop-color="var(--photo-garage-dark)"/>
      <stop offset="1" stop-color="var(--photo-garage)"/>
    </linearGradient>
    <linearGradient id="walkGrad" x1="0" y1="0" x2="0" y2="1">
      <stop offset="0" stop-color="#6a4a3a"/>
      <stop offset="0.5" stop-color="var(--photo-walk-light)"/>
      <stop offset="1" stop-color="var(--photo-walk)"/>
    </linearGradient>
    <filter id="headlineShadow" x="-5%" y="-20%" width="110%" height="140%">
      <feDropShadow dx="0" dy="2" stdDeviation="2" flood-color="#000" flood-opacity="0.7"/>
    </filter>
  </defs>

  <rect class="board-base" x="0" y="0" width="1120" height="373"/>

  <!-- Header panel -->
  <polygon points="528,0 1120,0 1120,129 490,129" fill="url(#headerGrad)"/>
  <text class="headline" x="561" y="60" filter="url(#headlineShadow)">Concrete Built</text>
  <text class="headline" x="639" y="108" filter="url(#headlineShadow)">For Generations</text>

  <!-- Project photos -->
  <polygon role="img" aria-label="Crew member placing fresh concrete on a residential job site" points="488,129 721,129 671,290 436,290" fill="url(#crewGrad)"/>
  <polygon role="img" aria-label="Finished concrete driveway in front of a brick two-car garage" points="728,129 949,129 891,290 678,290" fill="url(#garageGrad)"/>
  <polygon role="img" aria-label="Stamped terracotta-coloured concrete walkway leading to a house" points="955,129 1120,129 1120,290 896,290" fill="url(#walkGrad)"/>

  <!-- Company name -->
  <rect class="brand-square" x="197" y="56" width="60" height="60"/>
  <text class="company-name company-name--main" x="227" y="225" text-anchor="middle">MARLOWE’S</text>
  <text class="company-name company-name--sub" x="227" y="250" text-anchor="middle">CONSTRUCTION L.L.C</text>

  <!-- Phone band -->
  <polygon class="phone-band" points="0,290 434,290 407,373 0,373"/>
  <text class="tagline" x="227" y="312" text-anchor="middle">CONCRETE YOUR VISION!</text>
  <rect class="phone-icon-frame" x="35" y="316" width="40" height="40" rx="9"/>
  <path class="phone-icon" d="M46 325 l5 -2 l4 7 l-3 3 q3 6 9 9 l3 -3 l7 4 l-2 5 q-2 2 -6 1 q-13 -5 -18 -18 q-1 -4 1 -6 z"/>
  <text class="phone-number" x="86" y="352">555-214-7630</text>

  <!-- Review panel -->
  <polygon points="434,290 671,290 645,373 407,373" fill="url(#reviewGrad)"/>
  <text class="review-name" x="541" y="332" text-anchor="middle">Zorvix</text>
  <text class="review-rating" x="541" y="353" text-anchor="middle">rating ★★★★★</text>

  <!-- Website footer -->
  <polygon points="671,290 1120,290 1120,373 645,373" fill="url(#footerGrad)"/>
  <text class="website" x="688" y="338" textLength="300" lengthAdjust="spacingAndGlyphs">MarlowesConstruction.example</text>
  <text class="social-name" x="1008" y="331">Chatterly</text>
  <text class="social-name" x="1008" y="346">Pixtoria</text>
</svg>
</body>
</html>
```